Design clean technology service-based company website

Hello, We are looking to reskin our company website. We are an environmental inspection company and test for Asbestos, Lead and Mold along with other contaminants. People depend on the results to be accurate and fast. We are regulated by the EPA and State regulations. We work a lot with business to business and business to customer. We are wanting to make our new presentation to be modern and easy for customers to interact with us, understand our process and services while providing valuable environmental informational resource and updates. We are a technology based company and will be providing instantaneous results as reports come in for the customers. We are needing good calls to action on the site to direct them to setup a new inspection. Each user will have a backend access to their job information with invoices, reports, status, etc. We have developed software to be able to proved these reports and want to look the part.

My current website is www.trypelmarix.com

Helllo we are wanting to make sure we have good time to select the right website for us and also have the additional time to select other pages of the website. We have received great designs and have consolidated our requests into a document for the next set of iterations.

Target Market(s)

Home Owners, Contractors, Engineers, Real Estate Agents, Building Owners, Insurance Adjusters

Industry/Entity Type

Environmental Consultant

Number of Pages Required

5+ page

Font styles to use
Sans Serif

Colors
0355a3
9bcb3c
7f7f7f
f5f5f5
000000

Requirements
Must have
• Use our existing logo to design around
• The layouts look good in mobile mode for understanding and selecting services and signing up
• Clean Modern Layout
• Have all pages on the website have a similar layout and feel
• Clearly communicate services along with bundle service packages
• Detail the customer journey with graphic design
• Great call to actions to either schedule inspection online, call, text, chat
Nice to have
• Have an interactive graphic for where to test for lead, asbestos and mold.
• I like the barney kolts top order line bar - see attached
• Have clear question and answer page layouts for asbestos, lead and mold
• Show Company reviews
• Have clear Resources pages for all types of contaminants
Should not have
• My current website is www.trypelmarix.com

```html
<!DOCTYPE html>
<html lang="en">
<head>
<meta charset="UTF-8">
<title>Blog</title>
<link rel="stylesheet" href="https://fonts.googleapis.com/css2?family=Barlow:wght@400;500;600;700&family=Barlow+Semi+Condensed:wght@700&display=swap">
<style>
  :root {
    --green: #9bcb3c;
    --green-deep: #6aa55e;
    --grey: #7f7f7f;
    --grey-text: #6e6e6e;
    --grey-dark: #5e5e5e;
    --grey-light: #b5b5b5;
    --panel: #f5f5f5;
    --card: #f4f4f4;
    --white: #ffffff;
  }
  * { box-sizing: border-box; margin: 0; padding: 0; }
  html, body {
    width: 1200px; height: 1200px; overflow: hidden;
    background: var(--white);
    font-family: "Barlow", Arial, sans-serif;
    color: var(--grey-text);
  }
  .breadcrumb {
    height: 37px;
    background: var(--panel);
    border-top: 1px solid var(--green);
    display: flex; align-items: center; justify-content: center;
    font-size: 11.5px; color: var(--grey);
  }
  .page-title {
    margin-top: 46px;
    text-align: center;
    font-family: "Barlow Semi Condensed", "Arial Narrow", sans-serif;
    font-weight: 700;
    font-size: 50px;
    letter-spacing: 1px;
    line-height: 1;
    color: var(--grey);
  }
  .post-list {
    position: absolute; left: 230px; top: 193px;
    width: 737px;
    display: flex; flex-direction: column; gap: 19px;
  }
  .post {
    display: flex; height: 170px;
    background: var(--card);
    border-radius: 5px;
    overflow: hidden;
  }
  .post-media {
    position: relative;
    flex: 0 0 170px; height: 170px;
    background: linear-gradient(135deg, #93c43f 0%, #7eb24f 55%, var(--green-deep) 100%);
  }
  .post-media.photo {
    background: linear-gradient(135deg, #c9a98a 0%, #e7dccf 45%, #b98a62 100%);
  }
  .media-plus {
    position: absolute; left: 61px; top: 62px;
  }
  .post-body {
    padding: 18px 22px 0 19px;
    flex: 1;
  }
  .post-title {
    font-size: 11px; font-weight: 600;
    line-height: 14px;
    color: var(--grey-dark);
    margin-bottom: 13px;
  }
  .post.featured .post-title { color: var(--green); }
  .post-excerpt {
    font-size: 11px; line-height: 13.7px;
    color: var(--grey-text);
    margin-bottom: 7px;
  }
  .post-date {
    font-size: 11px; color: var(--grey-light);
    margin-bottom: 6px;
  }
  .read-more {
    display: inline-flex; align-items: center;
    font-size: 11.5px; color: var(--grey-text);
    text-decoration: none;
  }
  .read-more::before {
    content: ""; width: 1.5px; height: 9px;
    background: currentColor; margin-right: 7px;
  }
  .post.featured .read-more { color: var(--green); }
  .pagination {
    position: absolute; top: 1158px; left: 0; width: 1200px;
    display: flex; justify-content: center; align-items: center; gap: 7px;
    font-size: 11px; color: var(--grey-dark);
  }
  .pagination .current { color: var(--green); }
  .pagination .arrow { font-size: 11px; margin: 0 3px; }
</style>
</head>
<body>
  <nav class="breadcrumb">Home / Blog</nav>
  <h1 class="page-title">BLOG</h1>

  <main class="post-list">
    <article class="post featured">
      <div class="post-media photo" role="img" aria-label="Family smiling together on a wooden floor among moving boxes in a new home">
        <svg class="media-plus" width="48" height="48" viewBox="0 0 48 48" aria-hidden="true">
          <circle cx="24" cy="24" r="24" fill="#ffffff"/>
          <path d="M24 14v20M14 24h20" stroke="#9bcb3c" stroke-width="1.6"/>
        </svg>
      </div>
      <div class="post-body">
        <h2 class="post-title">Le arn What You Live In: 4 Reasons Get a Home Inspection for Asbestos, Lead Paint and Mold...</h2>
        <p class="post-excerpt">Phasellus viverra nulla ut metus varius laoreet. Quisque rutrum. Aenean imperdiet. Etiam ultricies nisi vel augue. Curabitur ullamcorper ultricies nisi. Nam eget dui. Etiam rhoncus. Maecenas tempus, tellus eget condimentum rhoncus, sem quam semper libero, sit amet adipiscing sem neque sed ipsum. Nam quam nunc, blandit vel, luctus pulvinar, hendrerit id, lorem. Maecenas nec odio et ante tincidunt tempus. Donec vitae sapien ut libero venenatis... faucibus. Nullam quis ante. Etiam sit amet orci eget eros</p>
        <p class="post-date">01 / 05 / 2018</p>
        <a class="read-more" href="#">Read more</a>
      </div>
    </article>

    <article class="post">
      <div class="post-media" role="img" aria-label="Blog post cover image"></div>
      <div class="post-body">
        <h2 class="post-title">Quisque rutrum. Aenean imperdiet. Etiam ultricies nisi vel augue. Curabitur ullamcorper ultricies nisi. Nam eget dui quam nunc, blandit vel, luctus pulvinar, hendrerit id, lorem.</h2>
        <p class="post-excerpt">Phasellus viverra nulla ut metus varius laoreet. Quisque rutrum. Aenean imperdiet. Etiam ultricies nisi vel augue. Curabitur ullamcorper ultricies nisi. Nam eget dui. Etiam rhoncus. Maecenas tempus, tellus eget condimentum rhoncus, sem quam semper libero, sit amet adipiscing sem neque sed ipsum. Nam quam nunc, blandit vel, luctus pulvinar, hendrerit id, lorem. Maecenas nec odio et ante tincidunt tempus.</p>
        <p class="post-date">01 / 05 / 2018</p>
        <a class="read-more" href="#">Read more</a>
      </div>
    </article>

    <article class="post">
      <div class="post-media" role="img" aria-label="Blog post cover image"></div>
      <div class="post-body">
        <h2 class="post-title">Nam quam nunc, blandit vel, luctus pulvinar, hendrerit id, lorem</h2>
        <p class="post-excerpt">Phasellus viverra nulla ut metus varius laoreet. Quisque rutrum. Aenean imperdiet. Etiam ultricies nisi vel augue. Curabitur ullamcorper ultricies nisi. Nam eget dui. Etiam rhoncus. Maecenas tempus, tellus eget condimentum rhoncus, sem quam semper libero, sit amet adipiscing sem neque sed ipsum. Nam quam nunc, blandit vel, luctus pulvinar, hendrerit id, lorem. Maecenas nec odio et ante tincidunt tempus. Donec vitae sapien ut libero venenatis... faucibus. Nullam quis ante. Etiam sit amet orci eget eros</p>
        <p class="post-date">01 / 05 / 2018</p>
        <a class="read-more" href="#">Read more</a>
      </div>
    </article>

    <article class="post">
      <div class="post-media" role="img" aria-label="Blog post cover image"></div>
      <div class="post-body">
        <h2 class="post-title">Quisque rutrum. Aenean imperdiet. Etiam ultricies nisi vel augue. Curabitur ullamcorper ultricies nisi. Nam eget dui quam nunc, blandit vel, luctus pulvinar, hendrerit id, lorem.</h2>
        <p class="post-excerpt">Phasellus viverra nulla ut metus varius laoreet. Quisque rutrum. Aenean imperdiet. Etiam ultricies nisi vel augue. Curabitur ullamcorper ultricies nisi. Nam eget dui. Etiam rhoncus. Maecenas tempus, tellus eget condimentum rhoncus, sem quam semper libero, sit amet adipiscing sem neque sed ipsum. Nam quam nunc, blandit vel, luctus pulvinar, hendrerit id, lorem. Maecenas nec odio et ante tincidunt tempus.</p>
        <p class="post-date">01 / 05 / 2018</p>
        <a class="read-more" href="#">Read more</a>
      </div>
    </article>

    <article class="post">
      <div class="post-media" role="img" aria-label="Blog post cover image"></div>
      <div class="post-body">
        <h2 class="post-title">Nam quam nunc, blandit vel, luctus pulvinar, hendrerit id, lorem</h2>
        <p class="post-excerpt">Phasellus viverra nulla ut metus varius laoreet. Quisque rutrum. Aenean imperdiet. Etiam ultricies nisi vel augue. Curabitur ullamcorper ultricies nisi. Nam eget dui. Etiam rhoncus. Maecenas tempus, tellus eget condimentum rhoncus, sem quam semper libero, sit amet adipiscing sem neque sed ipsum. Nam quam nunc, blandit vel, luctus pulvinar, hendrerit id, lorem. Maecenas nec odio et ante tincidunt tempus. Donec vitae sapien ut libero venenatis... faucibus. Nullam quis ante. Etiam sit amet orci eget eros</p>
        <p class="post-date">01 / 05 / 2018</p>
        <a class="read-more" href="#">Read more</a>
      </div>
    </article>
  </main>

  <nav class="pagination" aria-label="Pages">
    <span class="arrow">&lsaquo;</span>
    <span class="current">1</span>
    <span>2</span>
    <span>3</span>
    <span class="arrow">&rsaquo;</span>
  </nav>
</body>
</html>
```